Business Card - connecting 2 souls and beggining the journey of self discovery

Logo on the front
with tag line

On the back list of services and contact details

Seminars
workshops
Coaching
podcasts

Daniel Porthwick
Health & Wellbeing Life Coach
0491 372 815
daniel@wovenpathwellness.example
wovenpathwellness.example

Industry/Entity Type

Life Coaching

Contact Information for Business Card

I like the use of colour from the logo to be used. I'm not a fan of white.

Requirements
Must have
• My tagline: Every path inward begins with you
Nice to have
• Use of colour that is in the Woven Path Wellness logo

```html
<!DOCTYPE html>
<html lang="en">
<head>
<meta charset="utf-8">
<title>Woven Path Wellness – Business Card</title>
<link href="https://fonts.googleapis.com/css2?family=Carlito:ital,wght@0,400;0,700;1,700&display=swap" rel="stylesheet">
<style>
  :root {
    --page: #ffffff;
    --leaf: #8fc955;
    --leaf-light: #b3e65a;
    --leaf-deep: #82bf4a;
    --ink-green: #3cbc0c;
    --ink-white: #ffffff;
    --band: rgba(255, 255, 255, 0.82);
    --mark: #f2a93b;
  }
  * { margin: 0; padding: 0; box-sizing: border-box; }
  html, body {
    width: 1200px; height: 1200px; overflow: hidden;
    background: var(--page);
  }
  body { position: relative; font-family: "Carlito", "Calibri", sans-serif; }

  .card {
    position: absolute; left: 132px; width: 937px; height: 563px;
    overflow: hidden; color: var(--ink-white);
  }
  .card--front { top: 24px; }
  .card--back { top: 614px; }

  .card__texture {
    position: absolute; inset: 0;
    background:
      radial-gradient(ellipse 40% 45% at 8% 10%, var(--leaf-light) 0%, transparent 70%),
      radial-gradient(ellipse 30% 40% at 95% 95%, var(--leaf-light) 0%, transparent 70%),
      linear-gradient(135deg, var(--leaf) 0%, var(--leaf-deep) 100%);
  }

  .band {
    position: absolute; left: 0; right: 0;
    background: linear-gradient(90deg,
      rgba(255,255,255,0.15) 0%, var(--band) 22%, var(--band) 78%, rgba(255,255,255,0.15) 100%);
  }
  .card--front .band { top: 326px; height: 164px; }
  .card--back .band { top: 96px; height: 82px; }

  .centered { position: absolute; left: 0; right: 0; text-align: center; white-space: nowrap; }

  .brand-mark {
    position: absolute; left: 426px; top: 40px;
    width: 84px; height: 84px; border-radius: 50%; background: var(--mark);
  }
  .brand-name { top: 132px; font-size: 30px; font-weight: 400; line-height: 40px; }
  .brand-strap { top: 241px; font-size: 44px; font-weight: 400; line-height: 50px; }

  .tagline {
    top: 339px; color: var(--ink-green);
    font-size: 56px; font-weight: 700; font-style: italic; line-height: 70px;
  }

  .identity { top: 112px; color: var(--ink-green); line-height: 56px; }
  .identity__name { font-size: 52px; font-weight: 700; }
  .identity__divider { font-size: 38px; padding: 0 12px; }
  .identity__role { font-size: 33px; font-weight: 400; }

  .services { top: 226px; font-size: 43px; line-height: 50px; }
  .contact-phone { top: 302px; font-size: 60px; font-weight: 700; line-height: 64px; }
  .contact-email { top: 368px; font-size: 48px; line-height: 56px; }
  .contact-web { top: 426px; font-size: 48px; line-height: 56px; }
</style>
</head>
<body>
  <section class="card card--front">
    <div class="card__texture" role="img" aria-label="Soft green honeycomb background pattern"></div>
    <div class="brand-mark"></div>
    <p class="centered brand-name">Woven Path Wellness</p>
    <p class="centered brand-strap">Centre for Whole Wellbeing</p>
    <div class="band"></div>
    <p class="centered tagline">Every path inward<br>begins with you</p>
  </section>

  <section class="card card--back">
    <div class="card__texture" role="img" aria-label="Soft green honeycomb background pattern"></div>
    <div class="band"></div>
    <p class="centered identity">
      <span class="identity__name">Daniel Porthwick</span><span class="identity__divider">|</span><span class="identity__role">Health &amp; Wellbeing Life Coach</span>
    </p>
    <p class="centered services">• Seminars • workshops • Coaching • podcasts</p>
    <p class="centered contact-phone">0491 372 815</p>
    <p class="centered contact-email">daniel@wovenpathwellness.example</p>
    <p class="centered contact-web">wovenpathwellness.example</p>
  </section>
</body>
</html>
```